Design for Huddle app (online tool) (#102244)

Url of the app: http://huddle.moorfinch.dk

It currently has 3 main parts:
- Front: http://tealmarsh.dk/screencast/2015-12-01_12-53-36.png
- Dashboard: http://tealmarsh.dk/screencast/2015-12-01_12-54-16.png
- Meeting page: http://tealmarsh.dk/screencast/2015-12-01_12-54-53.png

The idea of the app is to have virtual meetings with other people, to take notes/minutes online and to share what is written.

Unregistered users can see only the front.

Registered users can see front, their own dashboard and the meetings which they created or to which they were invited.

The meeting itself has two roles - minute taker an attendee. The attendee can edit only the agenda so he should have different view for the other parts of the meeting compared to the minute taker who can edit everything.

In this doc it is described what are the elements per page which we want to have
https://files.quillnest.example/doc/7vKp2RtXw9LmQa4Hs8NcYe3BdZu6JfTgPo1iWxEk/edit?usp=sharing

As you can see, there is some inconsistency between the front page and the rest of the app. We would like to make it look professional and consistent on all places.

Goal: Get new responsive design where all main parts(front page, dashboard page, meeting page and profile page) will be consistent with each other.

The design should be clean, simple and with very friendly UX.
Updates

Industry/Entity Type

Online

Number of Pages Required

3 page

Font styles to use
Sans Serif

Requirements
Must have
• - Clean and simple
• - Very friendly UX

```html
<!DOCTYPE html>
<html lang="en">
<head>
<meta charset="utf-8">
<title>Plumvane Agenda – Sign up</title>
<link rel="stylesheet" href="https://fonts.googleapis.com/css2?family=Source+Sans+3:wght@300;400;600&display=swap">
<style>
  :root {
    --bg-deep: #262f3a;
    --bg-mid: #2c3642;
    --bg-soft: #333e4a;
    --text-light: #e6e9ec;
    --text-white: #ffffff;
    --placeholder: #5f6c7a;
    --rule: #8a939c;
    --accent-green: #7dc57b;
    --accent-amber: #f0a931;
    --button-text: #2a2f36;
    --mark: #8fa7c4;
  }
  * { box-sizing: border-box; margin: 0; padding: 0; }
  html, body { width: 1200px; height: 675px; overflow: hidden; }
  body {
    font-family: "Source Sans 3", "Source Sans Pro", sans-serif;
    background: var(--bg-mid);
    color: var(--text-light);
  }
  .page { position: relative; width: 1200px; height: 675px; overflow: hidden; }
  .backdrop {
    position: absolute; inset: 0;
    background:
      radial-gradient(ellipse at 20% 40%, var(--bg-soft) 0%, transparent 45%),
      radial-gradient(ellipse at 60% 80%, #303a46 0%, transparent 50%),
      linear-gradient(180deg, var(--bg-mid) 0%, var(--bg-deep) 100%);
  }
  .brand {
    position: absolute; left: 64px; top: 60px;
    display: flex; align-items: center; gap: 10px;
  }
  .brand-dot { width: 35px; height: 35px; border-radius: 50%; background: var(--mark); opacity: .8; }
  .brand-name { font-weight: 300; font-size: 20px; color: var(--text-light); letter-spacing: .2px; }
  .account-prompt {
    position: absolute; right: 64px; top: 71px;
    font-size: 16px; color: var(--text-white); font-weight: 400;
  }
  .account-prompt .login-link {
    color: var(--accent-green); text-decoration: none; margin-left: 16px; font-size: 16px;
  }
  .signup {
    position: absolute; left: 291px; top: 225px; width: 618px; text-align: center;
  }
  .signup-title { font-weight: 300; font-size: 28px; letter-spacing: .5px; color: var(--text-light); }
  .signup-lead { margin-top: 24px; font-weight: 300; font-size: 19px; line-height: 20px; color: var(--text-light); }
  .signup-form { margin-top: 18px; }
  .field {
    display: block; width: 100%; height: 40px;
    background: transparent; border: 0; border-bottom: 1px solid var(--rule);
    font-family: inherit; font-weight: 300; font-size: 19px; color: var(--text-light);
    padding: 0 12px; margin-bottom: 23px; outline: none;
  }
  .field::placeholder { color: var(--placeholder); }
  .create-button {
    display: inline-block; margin-top: 12px;
    width: 133px; height: 30px; border: 0; border-radius: 4px;
    background: var(--accent-amber); color: var(--button-text);
    font-family: inherit; font-weight: 600; font-size: 14px; letter-spacing: .2px;
    cursor: pointer;
  }
</style>
</head>
<body>
  <main class="page">
    <div class="backdrop" role="img" aria-label="Dimmed photo of a desk workspace with a potted plant, papers and a pen"></div>

    <header>
      <div class="brand">
        <span class="brand-dot"></span>
        <span class="brand-name">Plumvane Agenda</span>
      </div>
      <p class="account-prompt">Already have a Plumvane Agenda account?<a class="login-link" href="#">LOG IN</a></p>
    </header>

    <section class="signup">
      <h1 class="signup-title">SIGN UP</h1>
      <p class="signup-lead">Start your free 14-day trial today!<br>No credit card required - no risk.</p>
      <form class="signup-form">
        <input class="field" type="text" placeholder="First &amp; Last name">
        <input class="field" type="password" placeholder="Password">
        <input class="field" type="email" placeholder="Your email">
        <button class="create-button" type="button">CREATE ACCOUNT</button>
      </form>
    </section>
  </main>
</body>
</html>
```